Verlune Magician

I want the business card for my business to give to people who watch that later I will be employed to show magic here is my website http://www.verlunemagicien-exemple.fr/I want the interesting design , i am very opened for formal and informal, I watch a lot of design so don't stick to the common shape and form but i hope it can also be produced the thing to write on will be the same as in picture that i will upload , i also will upload the logo for you that so can be easy to useDenis CostilleMagicianMAGICIAN BALSAMO 17 rue des Tilleuls - 25000 BESANÇON contact@verlunemagicien-exemple.fr tel. 0381 476 093 tel. 0664 219 570

```html
<!DOCTYPE html>
<html lang="fr">
<head>
<meta charset="utf-8">
<title>Verlune Magician – Business Card</title>
<link href="https://fonts.googleapis.com/css2?family=Montserrat:wght@400;500;600&display=swap" rel="stylesheet">
<style>
  :root {
    --page-bg: #dcdcdc;
    --card-bg: #e9e9e9;
    --red: #d42a27;
    --ink: #111111;
    --grey: #6f6f6f;
    --font: "Montserrat", Arial, sans-serif;
  }
  * { box-sizing: border-box; margin: 0; padding: 0; }
  html, body { width: 1200px; height: 1200px; overflow: hidden; }
  body { background: var(--page-bg); font-family: var(--font); position: relative; }

  .card {
    position: absolute; left: 227px; width: 745px; height: 424px;
    background: var(--card-bg);
  }
  .card--front { top: 136px; }
  .card--back { top: 642px; }

  /* Front */
  .brand {
    position: absolute; left: 60px; top: 0; width: 210px; height: 424px;
    display: flex; align-items: center; justify-content: center;
  }
  .brand__name {
    font-size: 38px; font-weight: 400; letter-spacing: 1px; color: var(--ink);
  }
  .person__name {
    position: absolute; left: 350px; top: 70px;
    font-size: 23px; font-weight: 600; color: var(--red); letter-spacing: 0.5px;
  }
  .person__role {
    position: absolute; left: 350px; top: 101px;
    font-size: 16px; color: var(--grey);
  }
  .divider {
    position: absolute; left: 350px; right: 0; top: 152px;
    height: 2px; background: var(--red);
  }
  .company {
    position: absolute; left: 350px; top: 190px;
    font-size: 18px; font-weight: 500; color: var(--red); letter-spacing: 0.3px;
  }
  .address {
    position: absolute; left: 350px; top: 214px;
    font-size: 17px; color: var(--grey);
  }
  .contacts {
    position: absolute; left: 350px; top: 263px; list-style: none;
  }
  .contacts li {
    display: flex; align-items: center; height: 24px;
    font-size: 17px; color: var(--grey);
  }
  .contacts svg { width: 18px; height: 18px; margin-right: 8px; flex: none; }

  /* Back */
  .frame-line { position: absolute; background: var(--ink); }
  .frame-line--top { left: 92px; top: 59px; width: 571px; height: 3px; }
  .frame-line--bottom { left: 86px; top: 363px; width: 561px; height: 3px; }
  .frame-line--left { left: 52px; top: 104px; width: 3px; height: 226px; }
  .frame-line--right { left: 694px; top: 90px; width: 3px; height: 236px; }
  .suit { position: absolute; width: 50px; height: 50px; }
  .suit--spade { left: 32px; top: 37px; }
  .suit--heart { left: 668px; top: 31px; }
  .suit--diamond { left: 29px; top: 341px; }
  .suit--club { left: 664px; top: 339px; }
  .back-brand {
    position: absolute; left: 0; right: 0; top: 186px; text-align: center;
  }
</style>
</head>
<body>

<section class="card card--front">
  <div class="brand"><span class="brand__name">VERLUNE</span></div>

  <h1 class="person__name">LUCIEN MARBEC</h1>
  <p class="person__role">Magician</p>
  <div class="divider"></div>
  <h2 class="company">MAGICIAN VERLUNE</h2>
  <p class="address">17 rue des Tilleuls - 25000 BESANÇON</p>

  <ul class="contacts">
    <li>
      <svg viewBox="0 0 20 20"><circle cx="10" cy="10" r="10" fill="var(--red)"/><path d="M5 8 Q10 4 15 8 L14 10 L12 9 L12 8 Q10 7 8 8 L8 9 L6 10 Z M6 11 H14 V15 H6 Z" fill="#fff"/></svg>
      0381 476 093
    </li>
    <li>
      <svg viewBox="0 0 20 20"><circle cx="10" cy="10" r="10" fill="var(--ink)"/><rect x="6.5" y="4" width="7" height="12" rx="1.5" fill="#fff"/><rect x="7.8" y="5.5" width="4.4" height="8" fill="var(--ink)"/></svg>
      0664 219 570
    </li>
    <li>
      <svg viewBox="0 0 20 20"><circle cx="10" cy="10" r="10" fill="var(--red)"/><rect x="4.5" y="6" width="11" height="8" fill="none" stroke="#fff" stroke-width="1.4"/><path d="M4.5 6 L10 11 L15.5 6" fill="none" stroke="#fff" stroke-width="1.4"/></svg>
      contact@verlunemagicien-exemple.fr
    </li>
    <li>
      <svg viewBox="0 0 20 20"><circle cx="10" cy="10" r="10" fill="var(--ink)"/><circle cx="10" cy="10" r="6" fill="none" stroke="#fff" stroke-width="1.3"/><path d="M4 10 H16 M10 4 Q6 10 10 16 M10 4 Q14 10 10 16" fill="none" stroke="#fff" stroke-width="1.1"/></svg>
      www.verlunemagicien-exemple.fr
    </li>
  </ul>
</section>

<section class="card card--back">
  <div class="frame-line frame-line--top"></div>
  <div class="frame-line frame-line--bottom"></div>
  <div class="frame-line frame-line--left"></div>
  <div class="frame-line frame-line--right"></div>

  <svg class="suit suit--spade" viewBox="0 0 50 50"><path d="M25 3 C18 14 4 20 4 30 C4 37 12 41 21 35 L17 47 H33 L29 35 C38 41 46 37 46 30 C46 20 32 14 25 3 Z" fill="var(--ink)"/></svg>
  <svg class="suit suit--heart" viewBox="0 0 50 50"><path d="M25 47 C18 38 3 30 3 17 C3 8 10 3 16 3 C21 3 24 7 25 10 C26 7 29 3 34 3 C40 3 47 8 47 17 C47 30 32 38 25 47 Z" fill="var(--red)"/></svg>
  <svg class="suit suit--diamond" viewBox="0 0 50 50"><path d="M25 0 L50 25 L25 50 L0 25 Z" fill="var(--red)"/></svg>
  <svg class="suit suit--club" viewBox="0 0 50 50"><circle cx="25" cy="14" r="10" fill="var(--ink)"/><circle cx="13" cy="29" r="10" fill="var(--ink)"/><circle cx="37" cy="29" r="10" fill="var(--ink)"/><path d="M23 24 H27 L30 48 H20 Z" fill="var(--ink)"/></svg>

  <div class="back-brand"><span class="brand__name">VERLUNE</span></div>
</section>

</body>
</html>
```